New Book Cover Design Project: Belly Balance and Calm Stomachs

5-1/2 x8-1/2 inch cover front and back, with spine for a 45,000-word book.
Title: Belly Balance and Calm Stomachs. Subtitle: Restore Your Inner Garden and Leave Behind Bloating Woes, Slow Energy, Mental Haze, Extra Pounds, and Swelling—for a Brighter, Lighter Self. Author: Mavis Thornquill. Thorough discussion of how to achieve good digestion and lifelong gut health mainly through a quality diet based on real food free of chemicals. Ten chapters. I am author of nine other books, focused on vibrant health through natural living. I'm looking for a simple and impactful cover. My most recent book, also with cover from Pixel Harbor, is The Lone Pantry Plan: Reshape Your Bond with Meals in Only 30 Days.

Target Market(s)

Mostly middle aged women who want to feel better and have real solutions for their digestion and gut problems, including less midriff fat

Industry/Entity Type

Self-help health information from a nutritionist and family health advocate.

Font styles to use
Serif

Colors

Designer to choose colors to be used in the design.

Requirements
Must have
• Some way to indicate the author is a woman, my name being Mavis Thornquill. Multicolored, upbeat, with some graphic reference to gut health but not with an illustration of microbes or intestinesnGra
Nice to have
• Perhaps an image of women's flat bellies or before and after images of flat bellies, or anything else suggestive of a smooth-functioning living systempas
Should not have
• See above.

```html
<!DOCTYPE html>
<html lang="en">
<head>
<meta charset="utf-8">
<title>Belly Balance and Calm Stomachs — Mavis Thornquill</title>
<link rel="stylesheet" href="https://fonts.googleapis.com/css2?family=Archivo+Black&family=Great+Vibes&family=Tinos&display=swap">
<style>
  :root {
    --ink: #000000;
    --leaf: #47ab0a;
    --sun: #f7f200;
    --paper: #ffffff;
    --band-text: #111111;
    --shade-deep: #0a1408;
    --shade-mid: #1f3a1a;
    --glow: #8a4a1c;
  }
  html, body {
    margin: 0;
    padding: 0;
    overflow: hidden;
    background: var(--ink);
  }
  .cover {
    position: relative;
    width: 800px;
    height: 1200px;
    overflow: hidden;
    background: var(--ink);
  }
  .cover-photo {
    position: absolute;
    left: 0;
    top: 515px;
    width: 800px;
    height: 613px;
    background:
      radial-gradient(ellipse 240px 220px at 400px 300px, var(--glow) 0%, rgba(138,74,28,0.35) 45%, rgba(0,0,0,0) 75%),
      radial-gradient(ellipse 420px 360px at 400px 320px, var(--shade-mid) 0%, var(--shade-deep) 70%, var(--ink) 100%);
  }
  .title {
    position: absolute;
    left: 0;
    top: 0;
    width: 800px;
    height: 640px;
  }
  .title-main { font-family: "Archivo Black", sans-serif; fill: var(--leaf); }
  .title-join { font-family: "Great Vibes", cursive; fill: var(--sun); }
  .title-second { font-family: "Archivo Black", sans-serif; fill: var(--paper); }
  .subtitle {
    position: absolute;
    left: 40px;
    width: 720px;
    top: 984px;
    margin: 0;
    font-family: "Tinos", serif;
    font-size: 27.5px;
    line-height: 37px;
    color: var(--paper);
    text-align: center;
  }
  .author-band {
    position: absolute;
    left: 0;
    top: 1128px;
    width: 800px;
    height: 72px;
    background: var(--leaf);
    display: flex;
    align-items: center;
    justify-content: center;
  }
  .author-name {
    margin: 0;
    font-family: "Tinos", serif;
    font-size: 40px;
    letter-spacing: 0.42em;
    margin-right: -0.42em;
    color: var(--band-text);
    text-transform: uppercase;
  }
</style>
</head>
<body>
  <main class="cover">
    <div class="cover-photo" role="img" aria-label="Photo of a woman's hands cupping her midriff, with a glowing arrangement of broccoli, carrots, red cabbage, tomatoes and beans over her belly, against a dark green background"></div>

    <svg class="title" viewBox="0 0 800 640" aria-label="Belly Balance And Calm Stomachs">
      <text class="title-main" x="52" y="326" font-size="372" textLength="698" lengthAdjust="spacingAndGlyphs">BELLY</text>
      <text class="title-main" x="52" y="474" font-size="184" textLength="698" lengthAdjust="spacingAndGlyphs">BALANCE</text>
      <text class="title-join" x="378" y="548" font-size="118" text-anchor="middle">And</text>
      <text class="title-second" x="52" y="629" font-size="88" textLength="698" lengthAdjust="spacingAndGlyphs">CALM STOMACHS</text>
    </svg>

    <p class="subtitle">Restore Your Inner Garden and Leave Behind Bloating Woes, Slow Energy, Mental Haze, Extra Pounds, and Swelling—for a Brighter, Lighter Self.</p>

    <footer class="author-band">
      <p class="author-name">Mavis Thornquill</p>
    </footer>
  </main>
</body>
</html>
```